Bref créative
Business Cards, Letterhead and Email signature for Harlow Building Partners
Harlow Building Partners
Professional
Dale Merrick
Partner
Office: 4100 Ashgrove Ln Suite 800 Charlotte, NC 28226
Mailing: 5312 Ashgrove Ln #249 Charlotte, NC 28226
dmerrick@harlowbuildingpartners.example
harrlowbuildingpartners.example
I am open to ideas, maybe the logo with a matching background color. Be creative

```html
<!DOCTYPE html>
<html lang="en">
<head>
<meta charset="utf-8">
<title>Harlow Building Partners – Business Card</title>
<link rel="stylesheet" href="https://fonts.googleapis.com/css2?family=Open+Sans:wght@400;600;700&display=swap">
<style>
  :root {
    --page-bg: #e4e6ea;
    --navy-deep: #0f1a44;
    --navy: #1a2c6e;
    --royal: #1f4fa8;
    --royal-light: #2f66c4;
    --ink-blue: #1b2a8a;
    --grey-text: #555a63;
    --white: #ffffff;
    --silver-light: #e9ebef;
    --silver-mid: #aeb3bd;
    --silver-dark: #6c717c;
    --card-shadow: 0 10px 28px rgba(20, 28, 50, 0.28);
  }
  * { box-sizing: border-box; margin: 0; padding: 0; }
  html, body {
    width: 1200px; height: 699px; overflow: hidden;
    background: var(--page-bg);
    font-family: "Open Sans", Arial, sans-serif;
  }
  .canvas {
    position: relative; width: 1200px; height: 699px;
  }
  .card {
    position: absolute; top: 195px;
    width: 540px; height: 309px;
    border-radius: 3px; overflow: hidden;
    box-shadow: var(--card-shadow);
  }

  /* Back side */
  .card--back {
    left: 40px;
    background: radial-gradient(ellipse at 55% 35%, var(--royal) 0%, var(--navy) 45%, var(--navy-deep) 100%);
  }
  .card--back .artwork {
    position: absolute; left: 150px; top: 0; width: 390px; height: 309px;
    background: radial-gradient(ellipse at 45% 40%, rgba(178,184,214,0.55) 0%, rgba(120,128,170,0.3) 40%, rgba(30,40,90,0) 75%);
  }
  .card--back .web {
    position: absolute; left: 32px; top: 36px;
    color: var(--white); font-size: 14px; font-weight: 400; letter-spacing: 0.2px;
  }
  .card--back .brand {
    position: absolute; right: 26px; bottom: 30px;
    display: flex; align-items: center; gap: 8px;
    color: var(--white); font-size: 13px; font-weight: 700;
  }
  .card--back .brand-square {
    width: 12px; height: 12px; background: var(--white);
  }

  /* Front side */
  .card--front {
    left: 620px; background: var(--white);
  }
  .card--front .band {
    position: absolute; inset: 0;
  }
  .brand {
    position: absolute; left: 250px; top: 48px;
    display: flex; align-items: center; gap: 10px;
    color: var(--navy); font-size: 18px; font-weight: 700;
  }
  .brand-square {
    width: 30px; height: 30px; background: var(--navy);
  }
  .person {
    position: absolute; left: 34px; top: 92px;
  }
  .person-name {
    color: var(--ink-blue); font-size: 21px; font-weight: 700; line-height: 1.1;
  }
  .person-title {
    color: var(--grey-text); font-size: 13px; font-weight: 400; margin-top: 2px;
  }
  .contacts {
    position: absolute; left: 34px; top: 196px; right: 24px;
    color: var(--white); font-size: 11px; line-height: 1.45;
  }
  .address-row {
    display: flex; gap: 34px;
  }
  .address-label { font-weight: 700; }
  .contact-row {
    display: flex; gap: 20px; margin-top: 6px; flex-wrap: wrap;
  }
  .contact-item {
    display: flex; align-items: center; gap: 5px;
  }
  .contact-item svg { width: 11px; height: 11px; fill: var(--white); flex: none; }
</style>
</head>
<body>
<main class="canvas">

  <section class="card card--back" aria-label="Business card back">
    <div class="artwork" role="img" aria-label="Stepped silver chevron artwork"></div>
    <p class="web">www.harlowbuildingpartners.example</p>
    <div class="brand"><span class="brand-square"></span>Harlow Building Partners</div>
  </section>

  <section class="card card--front" aria-label="Business card front">
    <svg class="band" viewBox="0 0 540 309" preserveAspectRatio="none" aria-hidden="true">
      <defs>
        <linearGradient id="band-blue" x1="0" y1="0" x2="1" y2="1">
          <stop offset="0" stop-color="var(--royal-light)"/>
          <stop offset="1" stop-color="var(--navy)"/>
        </linearGradient>
        <linearGradient id="silver" x1="0" y1="0" x2="1" y2="0">
          <stop offset="0" stop-color="var(--silver-dark)"/>
          <stop offset="0.4" stop-color="var(--silver-light)"/>
          <stop offset="1" stop-color="var(--silver-mid)"/>
        </linearGradient>
      </defs>
      <path d="M0 186 Q30 168 80 160 L540 118 L540 309 L0 309 Z" fill="url(#band-blue)"/>
      <path d="M0 176 Q28 160 78 152 L540 110 L540 116 L80 158 Q30 166 0 184 Z" fill="url(#silver)"/>
      <path d="M0 190 Q32 172 82 164 L540 122 L540 126 L84 168 Q34 176 0 196 Z" fill="url(#silver)" opacity="0.8"/>
    </svg>

    <div class="brand"><span class="brand-square"></span>Harlow Building Partners</div>

    <div class="person">
      <p class="person-name">Dale Merrick</p>
      <p class="person-title">Partner</p>
    </div>

    <div class="contacts">
      <div class="address-row">
        <div class="address">
          <p class="address-label">Mailing:</p>
          <p>5312 Ashgrove Ln</p>
          <p>#249 Charlotte, NC 28226</p>
        </div>
        <div class="address">
          <p class="address-label">Office:</p>
          <p>4100 Ashgrove Ln</p>
          <p>Suite 800 Charlotte, NC 28226</p>
        </div>
      </div>
      <div class="contact-row">
        <span class="contact-item">
          <svg viewBox="0 0 24 24"><path d="M6.6 10.8a15.1 15.1 0 0 0 6.6 6.6l2.2-2.2c.3-.3.7-.4 1-.2 1.1.4 2.3.6 3.6.6.6 0 1 .4 1 1V20c0 .6-.4 1-1 1A17 17 0 0 1 3 4c0-.6.4-1 1-1h3.5c.6 0 1 .4 1 1 0 1.3.2 2.5.6 3.6.1.3 0 .7-.2 1z"/></svg>
          704 555 0193
        </span>
        <span class="contact-item">
          <svg viewBox="0 0 24 24"><path d="M7 2h10a2 2 0 0 1 2 2v16a2 2 0 0 1-2 2H7a2 2 0 0 1-2-2V4a2 2 0 0 1 2-2zm0 3v13h10V5zm5 14.2a1 1 0 1 0 0 2 1 1 0 0 0 0-2z"/></svg>
          704 555 0172
        </span>
        <span class="contact-item">
          <svg viewBox="0 0 24 24"><path d="M6 3h9l3 3v4h1a2 2 0 0 1 2 2v6h-3v3H6v-3H3v-6a2 2 0 0 1 2-2h1zm2 2v5h8V7h-2V5zm0 10v4h8v-4z"/></svg>
          704 555 0148
        </span>
      </div>
      <div class="contact-row">
        <span class="contact-item">
          <svg viewBox="0 0 24 24"><path d="M3 5h18v14H3zm2 2v.5l7 5 7-5V7zm14 3-7 5-7-5v7h14z"/></svg>
          dmerrick@harlowbuildingpartners.example
        </span>
        <span class="contact-item">
          <svg viewBox="0 0 24 24"><path d="M12 2a10 10 0 1 0 0 20 10 10 0 0 0 0-20zm6.9 9h-3a15 15 0 0 0-1.3-5.6A8 8 0 0 1 18.9 11zM12 4.1c.9 1.3 1.7 3.6 1.9 6.9h-3.8c.2-3.3 1-5.6 1.9-6.9zM9.4 5.4A15 15 0 0 0 8.1 11h-3a8 8 0 0 1 4.3-5.6zM5.1 13h3a15 15 0 0 0 1.3 5.6A8 8 0 0 1 5.1 13zm6.9 6.9c-.9-1.3-1.7-3.6-1.9-6.9h3.8c-.2 3.3-1 5.6-1.9 6.9zm2.6-1.3a15 15 0 0 0 1.3-5.6h3a8 8 0 0 1-4.3 5.6z"/></svg>
          www.harlowbuildingpartners.example
        </span>
      </div>
    </div>
  </section>

</main>
</body>
</html>
```